Stationery (Business Cards, Letterheads & Envelopes)

Require stationery design which includes the following items as a minimum.

- Business card design
- Letterhead
- Envelopes

Details for business card:
Logo: Main logo is called "tovell interiors square gold" but you may make use of whichever logo works best.
Tagline: Exquisite Furniture & Furnishings
Name: Mirren Oskaby
Title: Interior Stylist
Mobile: 0427 318 942
PH: 03 9512 3470
Email: mirren@tovell-interiors.com.au

Industry/Entity Type

Business

```html
<!DOCTYPE html>
<html lang="en">
<head>
<meta charset="utf-8">
<title>Tovell Interiors – Stationery</title>
<link href="https://fonts.googleapis.com/css2?family=Cinzel:wght@400&family=Open+Sans:wght@400;600&display=swap" rel="stylesheet">
<style>
  :root{
    --bg:#ececec;
    --paper:#f7f7f7;
    --ink:#1a1a1a;
    --black:#0d0d0d;
    --gold:#c9a544;
    --grey:#8a8a8a;
    --faint:#e9e9e9;
  }
  *{margin:0;padding:0;box-sizing:border-box}
  html,body{width:1200px;height:544px;overflow:hidden}
  body{background:radial-gradient(ellipse at 50% 45%,#f6f6f6 0%,var(--bg) 75%);position:relative;font-family:"Open Sans",sans-serif;color:var(--ink)}
  .brand{font-family:"Cinzel",serif;font-weight:400;letter-spacing:.08em;display:flex;align-items:center;gap:.4em;line-height:1}
  .brand .mark{display:inline-block;width:1.3em;height:1.3em;background:var(--gold)}
  .brand .name{display:flex;flex-direction:column;align-items:center}
  .brand .name small{font-size:.42em;letter-spacing:.3em;margin-top:.25em}
  .hero-brand{position:absolute;left:40px;top:62px;font-size:27px;color:var(--grey)}
  .hero-brand .mark{background:var(--grey)}
  .piece{position:absolute;box-shadow:0 2px 6px rgba(0,0,0,.18)}
  .card-front{left:280px;top:256px;width:122px;height:72px;background:var(--black);display:flex;flex-direction:column;align-items:center;justify-content:center}
  .card-front .mark{width:24px;height:24px;background:var(--gold)}
  .tagline{font-family:"Cinzel",serif;font-size:4px;letter-spacing:.08em;color:var(--gold);margin-top:10px}
  .card-back{left:281px;top:354px;width:122px;height:73px;background:var(--paper);padding:10px 8px}
  .card-back .brand{font-size:12px;color:var(--ink)}
  .card-back .mark{width:12px;height:12px}
  .person{margin-top:12px;font-size:5px;font-weight:600}
  .role{font-size:3.5px;color:var(--grey)}
  .contact{list-style:none;margin-top:4px;font-size:3.3px;line-height:1.5}
  .contact li::before{content:"";display:inline-block;width:2.5px;height:2.5px;border-radius:50%;background:var(--gold);margin-right:2px;vertical-align:middle}
  .social{position:absolute;right:10px;top:58px;display:flex;gap:2px}
  .social span{width:5px;height:5px;background:#5a8bb0}
  .faint-ornament{position:absolute;background:var(--faint)}
  .letterhead{left:465px;top:80px;width:268px;height:398px;background:var(--paper);padding:33px 32px}
  .letterhead .brand{font-size:17px}
  .letterhead .mark{width:20px;height:20px}
  .letterhead .faint-ornament{left:100px;top:110px;width:120px;height:90px;border-radius:50%;opacity:.7}
  .letter{position:relative;margin-top:54px;font-size:5px;line-height:1.45}
  .letter p{margin-bottom:6px}
  .signature{width:56px;height:20px;background:linear-gradient(90deg,#dcdcdc,#eeeeee)}
  .foot{position:absolute;left:0;bottom:0;width:100%;height:8px;display:flex}
  .foot .band{flex:1;background:var(--black);display:flex;align-items:center;justify-content:center}
  .foot .band span{font-family:"Cinzel",serif;font-size:4px;color:var(--gold);letter-spacing:.08em}
  .foot .accent{width:43px;background:var(--gold)}
  .dl-front{left:813px;top:147px;width:301px;height:149px;background:var(--black);padding:18px 24px;color:var(--gold)}
  .dl-front .brand{font-size:13px}
  .dl-front .mark{width:15px;height:15px}
  .dl-front .faint-ornament{right:0;top:0;width:78px;height:149px;background:linear-gradient(90deg,#0d0d0d,#2a2412)}
  .dl-back{left:817px;top:322px;width:299px;height:150px;background:var(--paper);overflow:hidden}
  .flap{position:absolute;left:0;top:0}
  .flap-text{position:absolute;left:0;right:0;top:36px;text-align:center;font-family:"Cinzel",serif;font-size:5px;letter-spacing:.08em;color:var(--gold)}
</style>
</head>
<body>

<div class="brand hero-brand"><span class="mark"></span><span class="name">TOVELL<small>INTERIORS</small></span></div>

<section class="piece card-front">
  <span class="mark"></span>
  <p class="tagline">EXQUISITE FURNITURE &amp; FURNISHINGS</p>
</section>

<section class="piece card-back">
  <div class="brand"><span class="mark"></span><span class="name">TOVELL<small>INTERIORS</small></span></div>
  <p class="person">MIRREN OSKABY</p>
  <p class="role">Interior Stylist</p>
  <ul class="contact">
    <li>0427 318 942</li>
    <li>03 9512 3470</li>
    <li>mirren@tovell-interiors.com.au</li>
  </ul>
  <div class="social"><span></span><span></span><span></span></div>
</section>

<section class="piece letterhead">
  <div class="brand"><span class="mark"></span><span class="name">TOVELL<small>INTERIORS</small></span></div>
  <div class="faint-ornament" role="img" aria-label="Faint brand ornament watermark"></div>
  <div class="letter">
    <p>28 June 2013</p>
    <p>[Insert Name and Address of Solicitor]</p>
    <p>Dear Mr/Ms [Solicitor Name]</p>
    <p><strong>[Insert Matter details]</strong></p>
    <p>In this matter [insert details of what happened]<br>[Insert who appeared for the Other Party]</p>
    <p>The following Orders were made;<br>1.&nbsp;&nbsp;&nbsp;&nbsp;&nbsp;&nbsp;&nbsp;[Insert Orders that were made]</p>
    <p>If I can assist you with anything further please do not hesitate to contact me.<br>I enclose a memorandum of fees for your attention.</p>
    <p>Yours faithfully</p>
    <div class="signature" role="img" aria-label="Handwritten signature"></div>
  </div>
  <div class="foot"><div class="band"><span>EXQUISITE FURNITURE &amp; FURNISHINGS</span></div><div class="accent"></div></div>
</section>

<section class="piece dl-front">
  <div class="brand"><span class="mark"></span><span class="name">TOVELL<small>INTERIORS</small></span></div>
  <div class="faint-ornament" role="img" aria-label="Large dark gold brand ornament"></div>
</section>

<section class="piece dl-back">
  <svg class="flap" width="299" height="150" viewBox="0 0 299 150">
    <path d="M0 0 H299 V20 L160 90 Q149.5 96 139 90 L0 20 Z" fill="#120f0d"/>
  </svg>
  <p class="flap-text">EXQUISITE FURNITURE &amp; FURNISHINGS</p>
</section>

</body>
</html>
```